Homepage for experience sharing site- interesting, fun and personable!

We need a homepage design for an experience sharing website. The tag line is 'find, promote and share great times!' The homepage should be exciting and innovative and illustrate the values of the site: possibility, freedom and life. It should be fun and personable.

To give you a clearer example, here are a few of the 'great times' users will be sharing on the site:

Club night, warehouse rave or beach gig
Antarctic expedition, Cambodian jungle trek
Cooking and surfing classes
Sumo speed dating
Drag racing and quad biking
Birthday parties, pub crawls and comedy nights

We like the idea of some sort of map or background image from which a few experiences pop up; however we are open to other ideas. The links below should give you an idea of the concept.

http://www.marbleco.example/cove#/cove-story
http://www.snaplume.example/map/
http://www.vidorama.example/watch?v=QK7TRW2pLzd
Updates

Hi,

please do not feel that your design must include a map, that was just an idea. If you can produce a design that delivers the message immediately and gets the user interested without a map then that is great! 

Please do not feel constrained.

Thanks,

Marisol

Hi,

I've created and attached two examples to the brief, which I hope will provide some guidance. I want the homepage design to concentrate on the human element and the concept of creating and sharing experiences.

Thanks,

Marisol  

Target Market(s)

18-37 age range. People who enjoy life and new experiences.

Industry/Entity Type

Racing

Requirements
Must have
• It must communicate the human element of the site... please see the attached examples I made as guidance

It must deliver the message as simply as possible

Could you ensure that your design includes the following elements please:

* breadcrumbs
* a search box
* the login and register should be part of the header block
Should not have
• Unnecessary elements

Only yellow

```html
<!DOCTYPE html>
<html lang="en">
<head>
<meta charset="utf-8">
<title>WildHours.com – Find, Promote, Share Great Times</title>
<link rel="stylesheet" href="https://fonts.googleapis.com/css2?family=Arimo:wght@400;700&family=Oswald:wght@500;600&family=Shadows+Into+Light&display=swap">
<style>
  :root {
    --yellow: #fff200;
    --yellow-deep: #f5d800;
    --yellow-btn-top: #fff45a;
    --yellow-btn-bottom: #f1cc00;
    --ink: #111111;
    --ink-soft: #222222;
    --red: #e8261c;
    --filter-top: #86aeb4;
    --filter-bottom: #5f8f98;
    --sky-top: #1f5fc8;
    --sky-mid: #4f8fe0;
    --sky-low: #b9d2ee;
    --panel: rgba(236, 242, 248, 0.86);
    --card: #eef3f7;
    --field: #ffffff;
    --field-line: #cfd8e0;
  }
  * { box-sizing: border-box; margin: 0; padding: 0; }
  html, body { width: 1200px; height: 820px; overflow: hidden; }
  body { position: relative; font-family: "Arimo", Arial, sans-serif; color: var(--ink); background: var(--yellow); }

  /* Header */
  .site-header {
    position: absolute; left: 0; top: 0; width: 1200px; height: 94px;
    background: linear-gradient(180deg, #fff64d 0%, var(--yellow) 60%, var(--yellow-deep) 100%);
  }
  .brand { position: absolute; left: 56px; top: 32px; display: flex; align-items: center; gap: 10px; }
  .brand-mark { width: 14px; height: 14px; border-radius: 50%; background: var(--ink); }
  .brand-name { font-family: "Arimo", Arial, sans-serif; font-weight: 700; font-size: 28px; line-height: 32px; color: var(--ink); }
  .header-slogan { position: absolute; left: 432px; top: 47px; font-family: "Oswald", sans-serif; font-weight: 600; font-size: 23px; line-height: 30px; color: var(--ink); letter-spacing: -0.3px; white-space: nowrap; }
  .account-links { position: absolute; left: 1082px; top: 16px; display: flex; flex-direction: column; gap: 6px; }
  .account-btn {
    display: block; width: 100px; height: 28px; border-radius: 4px; text-align: center;
    font: 700 13px/28px "Arimo", Arial, sans-serif; color: var(--ink); text-decoration: none;
    background: linear-gradient(180deg, var(--yellow-btn-top), var(--yellow-btn-bottom));
    border: 1px solid #d9b800; box-shadow: 0 1px 2px rgba(0,0,0,0.25);
  }

  /* Filter bar */
  .filter-bar {
    position: absolute; left: 0; top: 94px; width: 1200px; height: 52px;
    background: linear-gradient(180deg, var(--filter-top), var(--filter-bottom));
  }
  .filter-label { position: absolute; left: 15px; top: 20px; font: 700 10px/12px "Arimo", Arial, sans-serif; color: var(--yellow); }
  .filter-select {
    position: absolute; top: 10px; height: 30px; border-radius: 3px;
    background: linear-gradient(180deg, var(--yellow-btn-top), var(--yellow-btn-bottom));
    font: 700 13px/30px "Arimo", Arial, sans-serif; color: var(--ink-soft); padding-left: 14px;
  }
  .filter-select::after {
    content: ""; position: absolute; right: 0; top: 0; width: 30px; height: 30px;
    border-left: 1px solid #c9a800;
  }
  .filter-select svg { position: absolute; right: 10px; top: 12px; }
  .filter-country { left: 151px; width: 144px; }
  .filter-city { left: 308px; width: 144px; }
  .filter-type { left: 468px; width: 144px; }
  .filter-date { left: 627px; width: 144px; }
  .search-field {
    position: absolute; left: 911px; top: 105px; width: 237px; height: 30px; background: var(--field);
    border-radius: 2px; font: 400 11px/30px "Arimo", Arial, sans-serif; color: #333; padding-left: 13px;
  }
  .search-go { position: absolute; left: 1156px; top: 106px; width: 32px; height: 28px; background: #2a2a2a; border-radius: 3px; }
  .search-go svg { position: absolute; left: 11px; top: 8px; }

  /* Hero */
  .hero-sky {
    position: absolute; left: 0; top: 146px; width: 1200px; height: 617px;
    background:
      radial-gradient(ellipse 500px 160px at 300px 620px, rgba(235,242,250,0.9), transparent 70%),
      radial-gradient(ellipse 420px 140px at 1000px 640px, rgba(225,236,248,0.8), transparent 70%),
      linear-gradient(180deg, var(--sky-top) 0%, var(--sky-mid) 45%, var(--sky-low) 100%);
  }

  /* Sign-up panel */
  .signup-panel {
    position: absolute; left: 22px; top: 198px; width: 346px; height: 490px;
    background: var(--panel); border-radius: 8px; box-shadow: 0 2px 8px rgba(0,0,0,0.25);
  }
  .panel-close { position: absolute; left: 353px; top: 194px; }
  .panel-title { position: absolute; left: 18px; top: 20px; font: 700 26px/30px "Arimo", Arial, sans-serif; letter-spacing: -0.7px; color: var(--ink); white-space: nowrap; }
  .panel-intro { position: absolute; left: 20px; top: 61px; width: 300px; font: 400 12.5px/18px "Arimo", Arial, sans-serif; color: var(--ink-soft); }
  .btn-yellow {
    position: absolute; height: 34px; border-radius: 5px; text-align: center;
    font: 400 14px/34px "Arimo", Arial, sans-serif; color: var(--ink);
    background: linear-gradient(180deg, var(--yellow-btn-top), var(--yellow-btn-bottom));
    border: 1px solid #d9b800; box-shadow: 0 1px 2px rgba(0,0,0,0.25);
  }
  .btn-invite { left: 211px; top: 177px; width: 117px; }
  .btn-signup { left: 255px; top: 434px; width: 75px; }
  .signup-title { position: absolute; left: 19px; top: 214px; font: 700 26px/30px "Arimo", Arial, sans-serif; letter-spacing: -0.7px; }
  .signup-row { position: absolute; left: 21px; width: 310px; height: 30px; }
  .signup-row label { position: absolute; left: 0; top: 8px; font: 400 13px/14px "Arimo", Arial, sans-serif; color: var(--ink-soft); }
  .signup-row .field { position: absolute; left: 108px; top: 0; width: 200px; height: 28px; background: var(--field); border: 1px solid var(--field-line); border-radius: 2px; }

  /* Experience cards */
  .experience-card {
    position: absolute; width: 230px; height: 280px; background: var(--card);
    box-shadow: 0 2px 6px rgba(0,0,0,0.35);
  }
  .experience-photo { position: absolute; left: 14px; top: 14px; width: 202px; height: 208px; }
  .experience-host { position: absolute; left: 16px; top: 228px; font: 400 21px/24px "Shadows Into Light", cursive; color: #2a2a2a; }
  .experience-type { position: absolute; left: 18px; top: 256px; font: 400 13px/16px "Arimo", Arial, sans-serif; color: var(--ink); }
  .experience-link { position: absolute; right: 14px; top: 256px; font: 400 13px/16px "Arimo", Arial, sans-serif; color: var(--ink); }
  .experience-link::before { content: "▶ "; font-size: 9px; vertical-align: 1px; }

  .card-surf { left: 775px; top: 296px; }
  .card-sail { left: 588px; top: 163px; transform: rotate(0.5deg); }
  .card-cliff { left: 443px; top: 282px; transform: rotate(-0.5deg); }
  .card-dance { left: 948px; top: 155px; width: 228px; }
  .card-moto { left: 381px; top: 490px; }
  .card-party { left: 667px; top: 472px; transform: rotate(-0.5deg); }
  .card-comedy { left: 982px; top: 452px; transform: rotate(-0.5deg); }

  .photo-surf { background: linear-gradient(160deg, #1d8fa8, #3fb7c2 50%, #0f5a6e); }
  .photo-sail { background: linear-gradient(160deg, #3d7fd0, #a9c8ea 55%, #c33b2f 80%, #e6e6e6); }
  .photo-cliff { background: linear-gradient(180deg, #5d8fce, #a8c6e4 55%, #8b8b84); }
  .photo-dance { background: linear-gradient(160deg, #2f2a2e, #7c5f70 45%, #7ca04b 70%, #222); }
  .photo-moto { background: linear-gradient(180deg, #7fa4c6, #c9cdd0 45%, #a7916e 75%, #8a7350); }
  .photo-party { background: linear-gradient(160deg, #3a2a2a, #a7766a 45%, #5c4a45 75%, #1d1a1a); }
  .photo-comedy { background: linear-gradient(160deg, #0f0f12, #5b3a2a 55%, #231915); }

  /* Footer */
  .site-footer { position: absolute; left: 0; top: 763px; width: 1200px; height: 57px; background: var(--yellow); }
  .share-cta { position: absolute; left: 24px; top: 16px; display: flex; align-items: center; gap: 9px; font-family: "Oswald", sans-serif; font-weight: 500; font-size: 20px; line-height: 26px; color: var(--ink); text-decoration: none; }
  .footer-nav { position: absolute; right: 23px; top: 12px; display: flex; gap: 22px; }
  .footer-nav a { font: 400 13px/16px "Arimo", Arial, sans-serif; color: var(--ink); text-decoration: none; }
  .copyright { position: absolute; right: 23px; top: 34px; font: 700 10px/12px "Arimo", Arial, sans-serif; color: var(--ink); }
</style>
</head>
<body>

<header class="site-header">
  <div class="brand">
    <span class="brand-mark"></span>
    <span class="brand-name">WildHours.com</span>
  </div>
  <div class="header-slogan">FIND GREAT TIMES • PROMOTE GREAT TIMES • SHARE GREAT TIMES</div>
  <nav class="account-links">
    <a class="account-btn" href="#">LOGIN</a>
    <a class="account-btn" href="#">REGISTER</a>
  </nav>
</header>

<div class="filter-bar">
  <span class="filter-label">FILTER YOUR RESULTS</span>
  <div class="filter-select filter-country">Country - Any<svg width="11" height="6"><path d="M0 0h11L5.5 6z" fill="#222"/></svg></div>
  <div class="filter-select filter-city">City - Any<svg width="11" height="6"><path d="M0 0h11L5.5 6z" fill="#222"/></svg></div>
  <div class="filter-select filter-type">Type<svg width="11" height="6"><path d="M0 0h11L5.5 6z" fill="#222"/></svg></div>
  <div class="filter-select filter-date">Date - Any<svg width="11" height="6"><path d="M0 0h11L5.5 6z" fill="#222"/></svg></div>
</div>
<div class="search-field">Search People, Places &amp; Great Times</div>
<div class="search-go"><svg width="10" height="12"><path d="M1 0l8 6-8 6z" fill="#f5d800"/></svg></div>

<main>
  <div class="hero-sky" role="img" aria-label="Bright blue sky with drifting white clouds"></div>

  <section class="signup-panel">
    <h1 class="panel-title">Have you lived TODAY?</h1>
    <p class="panel-intro">Lorem ipsum dolor sit amet, consectetur adipisicing elit, sed do eiusmod tempor incididunt ut labore eter dolore magna aliqua. Ut enim ad minim veniam, quis nostrud exercitation ullamco laboris nisi ut aliquip ex ea exercitation ullamco commodo.&nbsp; ullamco laboris nisi ut aliquip ex ea commodo.</p>
    <div class="btn-yellow btn-invite">Invite a Friend</div>
    <h2 class="signup-title">Sign Up</h2>
    <div class="signup-row" style="top:255px"><label>First Name</label><div class="field"></div></div>
    <div class="signup-row" style="top:289px"><label>Last Name</label><div class="field"></div></div>
    <div class="signup-row" style="top:323px"><label>Your E-mail</label><div class="field"></div></div>
    <div class="signup-row" style="top:357px"><label>Password</label><div class="field"></div></div>
    <div class="signup-row" style="top:391px"><label>Re-Enter Email</label><div class="field"></div></div>
    <div class="btn-yellow btn-signup">Sign Up</div>
  </section>
  <svg class="panel-close" width="28" height="28" viewBox="0 0 28 28">
    <circle cx="14" cy="14" r="12.5" fill="#111" stroke="#fff" stroke-width="2"/>
    <path d="M9.5 9.5l9 9M18.5 9.5l-9 9" stroke="#fff" stroke-width="3" stroke-linecap="round"/>
  </svg>

  <article class="experience-card card-surf">
    <div class="experience-photo photo-surf" role="img" aria-label="Surfer riding inside a curling turquoise wave"></div>
    <span class="experience-host">Daniel Okafor</span><span class="experience-type">Stand-Up</span><span class="experience-link">View Details</span>
  </article>
  <article class="experience-card card-sail">
    <div class="experience-photo photo-sail" role="img" aria-label="Sailor in a red jacket on a yacht deck under a white sail"></div>
    <span class="experience-host">Daniel Okafor</span><span class="experience-type">Stand-Up</span><span class="experience-link">View Details</span>
  </article>
  <article class="experience-card card-cliff">
    <div class="experience-photo photo-cliff" role="img" aria-label="Hiker standing on a rocky cliff edge pointing at the sky"></div>
    <span class="experience-host">Daniel Okafor</span><span class="experience-type">Stand-Up</span><span class="experience-link">View Details</span>
  </article>
  <article class="experience-card card-dance">
    <div class="experience-photo photo-dance" role="img" aria-label="Friends dancing with raised arms at a club night"></div>
    <span class="experience-host">Daniel Okafor</span><span class="experience-type">Stand-Up</span><span class="experience-link">View Details</span>
  </article>
  <article class="experience-card card-moto">
    <div class="experience-photo photo-moto" role="img" aria-label="Motocross rider jumping a dirt bike over a dusty track"></div>
    <span class="experience-host">Daniel Okafor</span><span class="experience-type">Stand-Up</span><span class="experience-link">View Details</span>
  </article>
  <article class="experience-card card-party">
    <div class="experience-photo photo-party" role="img" aria-label="Group of young women celebrating at a party"></div>
    <span class="experience-host">Daniel Okafor</span><span class="experience-type">Stand-Up</span><span class="experience-link">View Details</span>
  </article>
  <article class="experience-card card-comedy">
    <div class="experience-photo photo-comedy" role="img" aria-label="Stand-up comedian performing with a microphone on a dark stage"></div>
    <span class="experience-host">Daniel Okafor</span><span class="experience-type">Stand-Up</span><span class="experience-link">View Details</span>
  </article>
</main>

<footer class="site-footer">
  <a class="share-cta" href="#">
    <svg width="16" height="22" viewBox="0 0 16 22"><path d="M3 2l9 9-9 9" fill="none" stroke="#e8261c" stroke-width="4"/></svg>
    CLICK HERE TO SHARE YOUR EXPERIENCE
  </a>
  <nav class="footer-nav">
    <a href="#">HOME</a><a href="#">ABOUT</a><a href="#">EXPERIENCE</a><a href="#">CONTACT US</a>
  </nav>
  <div class="copyright">Copyright © 2011 | WILD HOURS&nbsp; | ALL RIGHTS RESERVED</div>
</footer>

</body>
</html>
```